Brisbane IT support business needs our first letterhead (Contest)

Hello we are a Brisbane based Information Technology company providing support and services to small and medium sized businesses. We provide a range of services and solutions.

The business name is Kestrel Data Network Systems, or KDNS for short.

I am looking for a letterhead that looks professional (don't we all want that), but most importantly, it most utilize the colours in the logo attached, and any text used preferably in font type: HandelGotDBol.

```html
<!DOCTYPE html>
<html lang="en">
<head>
<meta charset="utf-8">
<title>KDNS Letterhead</title>
<link href="https://fonts.googleapis.com/css2?family=Jura:wght@500;700&family=Source+Sans+3:wght@300;400&display=swap" rel="stylesheet">
<style>
  :root {
    --backdrop: #9c9da0;
    --paper: #ffffff;
    --navy: #004560;
    --orange: #ee8033;
    --text: #6c6c6c;
    --text-dark: #555555;
    --mist: #dcdde0;
  }
  html, body {
    margin: 0;
    width: 1200px;
    height: 893px;
    overflow: hidden;
    background: var(--backdrop);
  }
  .letterhead {
    position: absolute;
    left: 290px;
    top: 51px;
    width: 613px;
    height: 792px;
    background: var(--paper);
    overflow: hidden;
    font-family: "Source Sans 3", sans-serif;
    font-weight: 300;
    color: var(--text);
  }
  .brand-name {
    position: absolute;
    left: 46px;
    top: 70px;
    margin: 0;
    font-family: "Jura", sans-serif;
    font-weight: 700;
    font-size: 18px;
    line-height: 1;
    letter-spacing: 0.3px;
    color: var(--navy);
  }
  .sender {
    position: absolute;
    right: 38px;
    top: 56px;
    text-align: right;
    font-family: "Jura", sans-serif;
    font-style: normal;
    font-weight: 500;
    font-size: 10px;
    line-height: 13px;
    color: var(--text-dark);
  }
  .sender .label { color: var(--orange); }
  .recipient, .salutation, .body-copy, .signoff {
    position: absolute;
    left: 86px;
    margin: 0;
  }
  .recipient {
    top: 232px;
    font-size: 11.6px;
    line-height: 14.4px;
    font-weight: 400;
  }
  .salutation {
    top: 347px;
    font-size: 11.6px;
    font-weight: 400;
  }
  .body-copy {
    top: 376px;
    width: 459px;
    font-size: 11.4px;
    line-height: 14.4px;
    text-align: justify;
  }
  .body-copy p { margin: 0 0 14.4px; }
  .scenery {
    position: absolute;
    left: 0;
    top: 560px;
    width: 613px;
    height: 208px;
    background: linear-gradient(to bottom, rgba(255,255,255,0) 0%, #eeeff0 35%, var(--mist) 100%);
  }
  .footer-rule {
    position: absolute;
    left: 0;
    top: 764px;
    width: 613px;
    height: 2px;
    background: var(--orange);
  }
  .footer-band {
    position: absolute;
    left: 0;
    top: 766px;
    width: 613px;
    height: 26px;
    background: var(--navy);
  }
  .signoff {
    top: 554px;
    font-size: 11.6px;
    color: var(--text-dark);
    font-weight: 300;
  }
  .signature {
    width: 90px;
    height: 42px;
    margin: 4px 0 2px -3px;
    background: linear-gradient(90deg, rgba(85,85,85,0.18), rgba(85,85,85,0.04));
    border-radius: 2px;
  }
  .web {
    position: absolute;
    left: 42px;
    top: 774px;
    font-family: "Jura", sans-serif;
    font-weight: 700;
    font-size: 9px;
    letter-spacing: 1px;
    color: var(--orange);
  }
</style>
</head>
<body>
  <main class="letterhead">
    <header>
      <h1 class="brand-name">Kestrel Data Network Systems</h1>
      <address class="sender">
        PO Box 318<br>
        Carindale, 4152<br>
        <span class="label">P.</span> 0412 730 264<br>
        <span class="label">E.</span> info@kestreldns.com
      </address>
    </header>

    <div class="scenery" role="img" aria-label="Pale city skyline with a suspension bridge"></div>
    <div class="footer-rule"></div>
    <div class="footer-band"></div>

    <section class="recipient">
      {client_contact_name}<br>
      {client_name}<br>
      {client_street_address1}<br>
      {client_street_address2}<br>
      {client_city}, {client_state} {client_postal}<br>
      {client_email}
    </section>

    <p class="salutation">Dear Mr. {client_last_name},</p>

    <section class="body-copy">
      <p>Lorem ipsum dolor sit amet, consectetur adipisicing elit, sed do eiusmod tempor incididunt ut labore et dolore magna aliqua. Ut enim ad minim veniam, quis nostrud exercitation ullamco laboris nisi ut aliquip ex ea commodo consequat. Duis aute irure dolor in reprehenderit in voluptate velit esse cillum dolore eu fugiat nulla pariatur.</p>
      <p>Lorem ipsum dolor sit amet, consectetur adipisicing elit, sed do eiusmod tempor incididunt ut labore et dolore magna aliqua. Ut enim ad minim veniam, quis nostrud exercitation ullamco laboris nisi ut aliquip ex ea commodo consequat. Duis aute irure dolor in reprehenderit in voluptate velit esse cillum dolore eu fugiat nulla pariatur. Excepteur sint occaecat cupidatat non proident, sunt in culpa qui officia deserunt mollit anim id est laborum.</p>
    </section>

    <section class="signoff">
      <div>Martin Hale</div>
      <div class="signature" role="img" aria-label="Handwritten signature"></div>
      <div>District Manager</div>
    </section>

    <footer class="web">www.kestreldns.com</footer>
  </main>
</body>
</html>
```